Make a dull looking powerpoint look very sharp

Dear Gigmaven,

Please take a look at the sales powerpoint that I have shared with you.
The powerpoint is 11 pages long.

I would like you to make the powerpoint look stunning using simple graphics to make the powerpoint look great and appealing to customers. We will send the powerpoint to our leads to explain to them what it is we can offer to them.

The text in the powerpoint is correct. So use the text that is provided on the powerpoint page.

I challenge you to come up with unique design that look professional and stunning for the eye.

If you have any question, please let me know.

I would like to see a total design, not only one page.

```html
<!DOCTYPE html>
<html lang="en">
<head>
<meta charset="utf-8">
<title>Fund Atlas – Partner Deck</title>
<link rel="stylesheet" href="https://fonts.googleapis.com/css2?family=Arimo:wght@400;700&display=swap">
<style>
:root{
  --page:#5b5b5b;
  --dark:#3c3c3c;
  --white:#ffffff;
  --blue:#2b9de0;
  --orange:#f26a3f;
  --ink:#1e1e1e;
  --grey:#5f5f5f;
  --quote-bg:#d8ecf8;
  --photo:#e0553f;
  --shot:#2e3138;
}
*{box-sizing:border-box;margin:0;padding:0}
html,body{width:729px;height:1200px;overflow:hidden;background:var(--page)}
body{font-family:"Arimo",Arial,sans-serif;position:relative}
.slide{position:absolute;width:314px;height:176px;background:var(--white);overflow:hidden}
.col-l{left:28px}.col-r{left:387px}
.row1{top:18px}.row2{top:211px}.row3{top:404px}.row4{top:597px}.row5{top:790px}.row6{top:996px}
.abs{position:absolute}
.dark{background:var(--dark);color:var(--white)}
.title{position:absolute;left:17px;top:14px;font-size:22px;color:var(--ink);font-weight:400}
.band{position:absolute;left:0;top:40px;height:28px;background:var(--blue);color:var(--white);font-weight:700;font-size:8px;display:flex;align-items:center;padding-left:32px;line-height:1.25}
.band::before{content:"";position:absolute;left:17px;top:50%;margin-top:-5px;border-left:6px solid var(--orange);border-top:5px solid transparent;border-bottom:5px solid transparent}
.body-text{position:absolute;font-size:6px;color:var(--ink);line-height:1.3}
.photo{position:absolute;width:75px;height:80px;background:linear-gradient(160deg,#ef6a4c,var(--photo));border:3px solid var(--white);box-shadow:0 1px 3px rgba(0,0,0,.35)}
.shot{position:absolute;background:linear-gradient(180deg,#2f3440,var(--shot))}
.map{position:absolute;inset:0;background:radial-gradient(ellipse at 55% 40%,rgba(255,255,255,.07),rgba(255,255,255,0) 70%)}
.blue-link{color:var(--blue);font-weight:700;font-size:7px}
.faq a{display:block;color:var(--blue);font-size:5.3px;text-decoration:underline;margin-bottom:8px;white-space:nowrap}
</style>
</head>
<body>

<!-- Cover -->
<section class="slide dark col-l row1">
  <div class="map" role="img" aria-label="Faint world map background"></div>
  <div class="abs" style="left:20px;top:52px;font-size:37px;font-weight:700;color:#1a3cf0;text-decoration:underline">FundAtlas.co</div>
  <div class="abs" style="left:0;top:130px;width:314px;height:39px;background:var(--white);color:var(--grey);font-size:13px;padding:6px 0 0 25px">Your voice to reach the founder community</div>
</section>

<!-- How does it work -->
<section class="slide col-r row1">
  <div class="title" style="font-size:17px;top:20px">How does it work?</div>
  <div class="band" style="top:58px;width:184px;height:28px">Startups visit Fund Atlas <span style="font-weight:400">&nbsp;to find</span></div>
  <div class="abs" style="left:32px;top:76px;font-size:6px;color:var(--white)">investors per country</div>
  <div class="abs" style="left:32px;top:96px;width:145px;font-size:6px;color:var(--blue);line-height:1.3">
    <p>On the country page <b>they see that you're a country partner</b></p>
    <p style="margin-top:6px"><b>Startups get massive value</b><br>from the free database "you" provide</p>
    <p style="margin-top:6px"><b>Provide targeted call2actions</b> and get startup leads on the country and investor pages</p>
  </div>
  <div class="shot" style="left:184px;top:0;width:130px;height:176px" role="img" aria-label="Website screenshot: Venture Capital Landscape in the Netherlands, powered by Northwind"></div>
</section>

<!-- Trend 1 -->
<section class="slide col-l row2">
  <div class="title">Trend</div>
  <div class="band" style="width:216px">9 out of 10 Companies are struggling to<br>connect with startups</div>
  <div class="abs" role="img" aria-label="Rocket line icon" style="left:20px;top:84px;width:48px;height:52px;background:#e6e6e6"></div>
  <div class="abs" style="left:83px;top:103px;font-size:9px;color:var(--ink);line-height:1.3">What if the startups<br>came to you?</div>
  <div class="abs dark" style="left:216px;top:0;width:98px;height:176px">
    <div class="abs" style="left:18px;top:12px;font-size:7.5px;font-weight:700;line-height:1.3">Fund<br>Atlas</div>
    <div class="abs" style="left:4px;top:46px;border-left:4px solid var(--white);border-top:4px solid transparent;border-bottom:4px solid transparent"></div>
    <div class="abs" style="left:14px;top:44px;width:84px;height:20px;background:#5e5e5e;font-size:7px;padding:2px 5px;line-height:1.25">Helps you to reach startup founders to</div>
    <div class="abs" style="left:16px;top:76px;font-size:6px;line-height:1.2">
      <p><span style="display:inline-block;width:9px;height:9px;border-radius:50%;background:var(--white);vertical-align:middle;margin-right:4px"></span>Make announcements</p>
      <p style="margin-top:9px"><span style="display:inline-block;width:9px;height:9px;border-radius:50%;background:var(--white);vertical-align:middle;margin-right:4px"></span>Sell your services</p>
      <p style="margin-top:9px"><span style="display:inline-block;width:9px;height:9px;border-radius:50%;background:var(--white);vertical-align:middle;margin-right:4px"></span>Spread your events</p>
    </div>
    <div class="abs" style="left:16px;top:130px;width:68px;height:1px;background:var(--white)"></div>
    <div class="abs" style="left:16px;top:145px;font-size:5.8px;line-height:1.3">We are inviting you to<br>join our partner program</div>
  </div>
</section>

<!-- Benefits -->
<section class="slide col-r row2">
  <div class="shot" style="left:0;top:0;width:130px;height:176px" role="img" aria-label="Website screenshot: Venture Capital Landscape in the Netherlands, sponsored by Rivermart"></div>
  <div class="abs" style="left:140px;top:26px;line-height:1.3">
    <p class="blue-link">Reach your startup audience</p>
    <p class="blue-link" style="margin-top:18px">Bring value to your startup<br>audience</p>
    <p class="blue-link" style="margin-top:18px">Support the startup ecosystem</p>
    <p class="blue-link" style="margin-top:18px">Spread your personal message</p>
    <p class="blue-link" style="margin-top:18px">Use your custom call2actions</p>
  </div>
</section>

<!-- Trend 2 -->
<section class="slide col-l row3">
  <div class="title">Trend</div>
  <div class="band" style="width:314px">“We're only really at the stage where people are learning to walk”</div>
  <div class="abs" style="left:32px;top:87px;width:156px;height:52px;background:var(--quote-bg);border-radius:3px;padding:6px 14px;font-size:5.2px;color:var(--ink);line-height:1.3">
    <span class="abs" style="left:3px;top:-2px;font-size:20px;color:var(--blue);font-weight:700">“</span>
    Large corporates are realizing they need to engage on a formal basis and have someone at the organization whose job or part of their job is to engage with emerging tech and startups
    <p style="margin-top:4px;font-size:4px;color:var(--grey)">Lena Marsh - founder and lead of the Ledgerly Startup Challenge in London</p>
    <span class="abs" style="right:3px;bottom:-8px;font-size:20px;color:var(--blue);font-weight:700">”</span>
  </div>
  <div class="photo" style="left:210px;top:74px" role="img" aria-label="Portrait photo of the quoted founder against a red wall"></div>
</section>

<!-- Live demo -->
<section class="slide dark col-r row3">
  <div class="abs" style="left:70px;top:54px;width:178px;height:62px;border:1.5px solid var(--orange);border-radius:9px;display:flex;align-items:center;justify-content:center;color:var(--orange);font-weight:700;font-size:14px">Click for live demo &gt;</div>
</section>

<!-- Opportunity -->
<section class="slide col-l row4">
  <div class="title">Opportunity</div>
  <div class="band" style="width:314px">Be a driving force on the platform that startup founders love</div>
  <div class="body-text" style="left:44px;top:103px;width:150px">
    <p>People naturally trust parties that support the communities they are a part of.</p>
    <p style="margin-top:12px">What if we could help you to build that trust and help you spread your companies voice at the same time?</p>
  </div>
  <div class="photo" style="left:210px;top:74px" role="img" aria-label="Portrait photo against a red wall"></div>
</section>

<!-- Partner steps + FAQ -->
<section class="slide col-r row4">
  <div class="abs" style="left:8px;top:18px;font-size:15px;color:var(--ink)">I want to become a partner</div>
  <div class="band" style="top:42px;width:212px">Follow three simple steps</div>
  <div class="abs" style="left:28px;top:78px;width:180px;font-size:5.5px;color:var(--ink);line-height:1.3">
    <p style="position:relative;padding-left:16px"><span class="abs" style="left:0;top:-2px;font-size:14px;color:var(--blue)">1.</span>Go to <span style="color:#1a3cf0;text-decoration:underline">this link</span> and pick the countries you want to sponsor</p>
    <p style="position:relative;padding-left:16px;margin-top:11px"><span class="abs" style="left:0;top:-2px;font-size:14px;color:var(--blue)">2.</span>At the bottom of the page tell us which countries you would like to support and we will send you the price list for those countries</p>
    <p style="position:relative;padding-left:16px;margin-top:7px"><span class="abs" style="left:0;top:-2px;font-size:14px;color:var(--blue)">3.</span>We agree on the partnership and we go into the procces of incorporating your branding and your call2actions into the countries you choose to support</p>
  </div>
  <div class="abs dark faq" style="left:212px;top:0;width:102px;height:176px;padding:11px 0 0 6px">
    <p style="font-size:7px;font-weight:700;margin-bottom:8px">FAQ</p>
    <a>What is FundAtlas.co?</a>
    <a>Why was FundAtlas.co built?</a>
    <a>Why should I support Fund Atlas?</a>
    <a>What is the mission of Fund Atlas?</a>
    <a>How can I use Fund Atlas to reach<br>startups?</a>
    <a>Why do startups love Fund Atlas?</a>
    <a>When will it go live?</a>
    <a>How do you differ from<br>DealGrid, SeedRoster and venturedex.io?</a>
  </div>
</section>

<!-- Solution -->
<section class="slide col-l row5">
  <div class="title">Solution</div>
  <div class="band" style="width:314px">Fund Atlas is an online tool to find venture funding that is<br>supported by companies that want to reach startups</div>
  <div class="body-text" style="left:32px;top:78px;width:160px">
    <p>We help startup to find venture funding for free based on stage, industry and country</p>
    <p style="margin-top:7px">We help companies to reach this highly targeted audience by sponsoring website real-estate</p>
  </div>
  <div class="abs" style="left:35px;top:127px;font-size:7px;font-weight:700;color:var(--blue);line-height:1.3">In<br>Short,</div>
  <div class="body-text" style="left:62px;top:126px;width:100px">By supporting Fund Atlas you support your local startup community</div>
  <div class="abs" style="left:32px;top:149px;width:118px;height:1px;background:var(--orange)"></div>
  <div class="photo" style="left:210px;top:74px" role="img" aria-label="Portrait photo against a red wall"></div>
</section>

<!-- Closing -->
<section class="slide dark col-r row5">
  <div class="map" role="img" aria-label="Faint world map background"></div>
  <div class="abs" style="left:6px;top:14px;font-size:38px;font-weight:700;line-height:1.13">Fund<br>Atlas</div>
  <div class="abs" style="left:6px;top:133px;font-size:12.5px">Support startups by bringing them true value</div>
</section>

<!-- Why now -->
<section class="slide col-l row6">
  <div class="title">Why now?</div>
  <div class="band" style="width:158px">Traditional strategies to reach<br>startups fall short</div>
  <div class="body-text" style="left:20px;top:76px;width:130px">
    <p>Efforts limited by:</p>
    <p style="margin-top:10px">The lack of trust startups have in corporates</p>
    <p style="margin-top:10px">A lack of value that you bring when spreading your message</p>
  </div>
  <div class="abs dark" style="left:158px;top:0;width:156px;height:176px">
    <div class="abs" style="left:8px;top:46px;border-left:5px solid var(--white);border-top:5px solid transparent;border-bottom:5px solid transparent"></div>
    <div class="abs" style="left:19px;top:44px;font-size:7.5px;font-weight:700;color:var(--blue);line-height:1.3">Become a Fund Atlas Partner<br>and unlock the ability to:</div>
    <div class="abs" style="left:19px;top:82px;width:130px;font-size:5.5px;line-height:1.3">
      <p>Increase trust startup founders have in your brand</p>
      <p style="margin-top:6px">Increase your overall brand awareness with in the startup community</p>
      <p style="margin-top:6px">Spread your message to startups on a steady and predictable basis</p>
    </div>
  </div>
</section>

</body>
</html>
```